Corrabeen Holiday Village Flyer Project

Flyer required for a holiday caravan park. I have attached the current flyer for the park and would like to use the same layout. Please also alter the changes to the text that I have marked up. Until the additional uploads for the new images are ready, could you please just leave those as a blank square and the images can be inserted once I have them loaded.

Target Market(s)

Holiday makers

Industry/Entity Type

Tourism

Colors
3176b5
33a6d7
0393ce
fbee3e
fbed22
ffffff
faa54b

Requirements
Must have
• copy the attached flyer
• Would like a better title font for the front text - "Corrabeen Holiday Village", please make that a more playful holiday feel font
• Please use images 001 & 002 as the front cover images
• I have more images to load up which will be done 4/7.
Nice to have
• would like a better colour back ground to the flyer, maybe blue-ish and then alter the colour of the text accordingly
Should not have
• Please use the attached flyer copy as a template

```html
<!DOCTYPE html>
<html lang="en">
<head>
<meta charset="utf-8">
<title>Corrabeen Holiday Village – Tri-fold Flyer</title>
<link rel="stylesheet" href="https://fonts.googleapis.com/css2?family=Arimo:wght@400;700&family=Ubuntu:wght@400;500;700&family=Open+Sans:wght@400&family=Kalam:wght@700&display=swap">
<style>
:root{
  --page:#0a4a7c;
  --navy:#2f68ad;
  --brand:#1aa3d8;
  --sky:#33a6d7;
  --link:#3bb6e2;
  --pale:#cfe9f7;
  --grey:#dcdcdc;
  --ink:#1d2b36;
  --white:#ffffff;
}
*{margin:0;padding:0;box-sizing:border-box}
html,body{width:920px;height:1200px;overflow:hidden}
body{background:var(--page);font-family:Arimo,Arial,sans-serif;color:var(--ink);position:relative}
.panel{position:absolute;width:266px;overflow:hidden}
.row-top{top:32px;height:563px}
.row-bottom{top:604px;height:564px}
.col-1{left:53px}.col-2{left:319px}.col-3{left:585px}
.abs{position:absolute}
.photo{position:absolute;left:0;width:266px}
.wave{position:absolute;left:0;width:266px}

/* panel: location */
.location{background:var(--white)}
.map{left:45px;top:16px;width:165px;height:232px;background:linear-gradient(160deg,#6cc7cc,#8fd27a 70%,#b9d57a);border:1px solid #dff}
.intro{left:25px;top:272px;width:216px;font-size:10px;line-height:12.3px;text-align:justify}
.attractions{left:22px;top:358px;width:222px;border-collapse:collapse;font-family:"Open Sans",sans-serif;font-size:9.6px;background:#eef2f3;table-layout:fixed}
.attractions col.a{width:106px}
.attractions td{padding:3px 10px;border-bottom:1px solid #fff;vertical-align:top;line-height:12px}
.attractions td:first-child{border-right:1px solid #cfd6d8}
.banner{left:0;top:504px;width:266px;height:48px;background:var(--navy);color:var(--white);font-family:Ubuntu,sans-serif;font-weight:500;font-size:12px;text-align:center;padding-top:10px;line-height:15px}

/* shared brand name */
.brand-name{text-align:center;font-family:Kalam,cursive;font-weight:700;color:var(--brand);line-height:1}
.brand-name .word{display:block;font-size:42px}
.brand-name .sub{display:block;font-size:15px;letter-spacing:4px;margin-top:2px}

/* panel: contact */
.contact{background:radial-gradient(ellipse at 50% 35%,#fafafa,#e3e3e3 80%)}
.contact .brand-name{left:0;top:164px;width:266px}
.details{left:0;width:266px;text-align:center;font-size:12.5px;line-height:16px}
.details .phone{color:var(--link);font-size:16px;line-height:18px;margin-bottom:5px}
.details .web{color:var(--link);font-weight:700;font-size:11.5px;margin-top:4px}
.social{left:0;width:266px;display:flex;justify-content:center;gap:3px}
.social span{width:18px;height:18px;border-radius:50%;background:var(--sky)}

/* panel: cover */
.cover{background:var(--grey)}
.cover .brand-name{left:0;top:30px;width:266px;color:var(--white);z-index:2}

/* panel: activities */
.activities{background:var(--white);text-align:center}
.heading{font-family:Ubuntu,sans-serif;font-weight:700;font-size:19px;color:var(--brand)}
.activities .heading{position:absolute;left:0;top:36px;width:266px}
.lead{position:absolute;left:0;width:266px;font-family:"Open Sans",sans-serif;font-size:10.5px}
.pairs{position:absolute;left:24px;width:222px;display:grid;grid-template-columns:1fr 1fr;font-family:"Open Sans",sans-serif;font-size:10px;line-height:13.7px;color:var(--link)}
.single{position:absolute;left:0;width:266px;font-family:"Open Sans",sans-serif;font-size:10px;line-height:13.7px;color:var(--link)}
.tagline{position:absolute;left:0;top:254px;width:266px;font-family:Kalam,cursive;font-weight:700;font-size:22px;line-height:22px;color:var(--link)}

/* panel: accommodation */
.accommodation{background:var(--pale)}
.accommodation .heading{position:absolute;left:34px;top:202px}
.bullets{position:absolute;list-style:none;font-size:11px;line-height:19.4px}
.bullets li::before{content:"•";display:inline-block;width:12px;color:var(--ink)}
.bullets li:nth-child(odd)::before{color:var(--link)}
.accommodation .bullets{left:33px;top:238px}

/* panel: facilities */
.facilities{background:var(--white)}
.facilities .heading{position:absolute;left:29px;top:38px}
.facilities .bullets{left:29px;top:70px}
.facilities .bullets li:nth-child(odd){color:var(--link)}
.nearby{position:absolute;left:22px;top:252px;font-size:12.3px;line-height:15.2px;color:var(--link)}
.nearby span{display:inline-block;width:20px;text-align:right;margin-right:5px}
</style>
</head>
<body>

<!-- outside: location -->
<section class="panel row-top col-1 location">
  <svg class="wave" style="top:120px;height:443px" viewBox="0 0 266 443" preserveAspectRatio="none" aria-hidden="true">
    <defs><linearGradient id="aquaFill" x1="0" y1="0" x2="0" y2="1"><stop offset="0" stop-color="#86d6e8"/><stop offset="1" stop-color="#58c1dc"/></linearGradient></defs>
    <path d="M0 14 C60 -6 140 0 266 20 L266 443 L0 443 Z" fill="url(#aquaFill)"/>
    <path d="M0 30 C10 8 40 0 80 4" fill="none" stroke="#2a9fd6" stroke-width="4"/>
  </svg>
  <div class="abs map" role="img" aria-label="Simple street map showing the park between the beach and the estuary, off the coast road"></div>
  <p class="abs intro">We are the second turn to the left, after the bridge. Ideally located nestled between Melrose Beach and the Estuary, 3mins south of the Corrabeen cut with all the the associated water activities and 15mins from Mandurah CBD boasting a range of activities such as</p>
  <table class="abs attractions">
    <colgroup><col class="a"><col></colgroup>
    <tr><td>Summer Concerts</td><td>Foreshore Markets</td></tr>
    <tr><td>Festivals</td><td>Bayside Performing Arts Centre</td></tr>
    <tr><td>Art Gallery</td><td>Wineries</td></tr>
    <tr><td>Dolphin Tours</td><td>Wildlife parks</td></tr>
    <tr><td>Movie theatres</td><td>Taverns</td></tr>
    <tr><td>Superb Restaurants</td><td>Night Clubs</td></tr>
  </table>
  <div class="abs banner">HISTORICAL SITES &amp; MANY MORE<br>TOURIST ATTRACTIONS!</div>
</section>

<!-- outside: contact -->
<section class="panel row-top col-2 contact">
  <div class="abs brand-name"><span class="word">Corrabeen</span><span class="sub">HOLIDAY VILLAGE</span></div>
  <div class="abs details" style="top:252px">
    <div class="phone">Ph : (08) 9500 2614</div>
    <div>212 Shoreline Rd Corrabeen</div>
    <div>info@corrabeenholiday.com.au</div>
    <div class="web">www.corrabeenholiday.com.au</div>
  </div>
  <div class="abs social" style="top:354px"><span></span><span></span><span></span></div>
</section>

<!-- outside: cover -->
<section class="panel row-top col-3 cover">
  <div class="photo" style="top:0;height:400px;background:linear-gradient(180deg,#3f7fc4 0%,#7fb2e0 40%,#9cc9e6 70%,#6c8f9e 100%)" role="img" aria-label="Children jumping off the deck of a houseboat into the water"></div>
  <div class="abs brand-name"><span class="word">Corrabeen</span><span class="sub">HOLIDAY VILLAGE</span></div>
  <svg class="wave" style="top:350px;height:80px" viewBox="0 0 266 80" preserveAspectRatio="none" aria-hidden="true">
    <path d="M0 40 C70 10 160 20 266 50 L266 80 L0 80 Z" fill="var(--grey)"/>
    <path d="M0 40 C70 12 160 20 266 46" fill="none" stroke="#0f5ea8" stroke-width="5"/>
    <path d="M0 30 C70 4 160 14 266 38" fill="none" stroke="#33b7e6" stroke-width="4"/>
  </svg>
  <div class="abs details" style="top:432px">
    <div class="phone">Ph : (08) 9500 2614</div>
    <div>212 Shoreline Rd Corrabeen</div>
    <div>info@corrabeenholiday.com.au</div>
    <div class="web">www.corrabeenholiday.com.au</div>
  </div>
  <div class="abs social" style="top:520px"><span></span><span></span><span></span></div>
</section>

<!-- inside: activities -->
<section class="panel row-bottom col-1 activities">
  <h2 class="heading">WHAT TO DO?</h2>
  <p class="lead" style="top:60px">The Estuary is only 2 mins to the east for</p>
  <div class="pairs" style="top:79px"><span>Water Sports</span><span>Swimming</span><span>Crabbing</span><span>Prawning</span><span>Boating</span><span>Boat Ramp Access</span></div>
  <p class="lead" style="top:125px">Melrose Beach is 5mins to the west for</p>
  <div class="pairs" style="top:144px"><span>Water Skiing</span><span>Sailing</span><span>Swimming</span><span>Fishing</span><span>Crabbing</span><span>Surfing</span><span>Boat Ramp Access</span><span>Veach walking</span></div>
  <p class="lead" style="top:206px">Sporting facilities 5mins</p>
  <div class="single" style="top:222px">Golfing<br>Bowls</div>
  <p class="tagline">The best crabbing<br>in Mandurah</p>
  <div class="photo" style="top:336px;height:228px;background:linear-gradient(180deg,#e9eef0,#b9c2c4 50%,#6b8a8e)" role="img" aria-label="Family crabbing with nets from a wooden jetty"></div>
  <svg class="wave" style="top:314px;height:36px" viewBox="0 0 266 36" preserveAspectRatio="none" aria-hidden="true">
    <path d="M0 0 L266 0 L266 18 C180 0 80 4 0 30 Z" fill="var(--white)"/>
    <path d="M0 28 C80 2 180 0 266 16" fill="none" stroke="#33b7e6" stroke-width="5"/>
  </svg>
</section>

<!-- inside: accommodation -->
<section class="panel row-bottom col-2 accommodation">
  <div class="photo" style="top:0;height:176px;background:linear-gradient(180deg,#6f7880 0%,#e0a66a 28%,#2c3a4a 40%,#1b2a3a 100%)" role="img" aria-label="Sunset over the ocean with a person standing on the rocks"></div>
  <svg class="wave" style="top:140px;height:50px" viewBox="0 0 266 50" preserveAspectRatio="none" aria-hidden="true">
    <path d="M0 24 C70 -4 170 10 266 42 L266 50 L0 50 Z" fill="var(--pale)"/>
    <path d="M0 22 C70 -6 170 8 266 38" fill="none" stroke="#33b7e6" stroke-width="4"/>
  </svg>
  <h2 class="heading">ACCOMMODATION</h2>
  <ul class="bullets">
    <li>Chalets Ensuite &amp; Air Con</li>
    <li>Caravans</li>
    <li>Caravans &amp; Air Con</li>
    <li>Caravans Ensuite &amp; Air Con</li>
    <li>Powered Sites</li>
  </ul>
  <div class="photo" style="top:370px;height:194px;background:linear-gradient(180deg,#bfe0f2 0%,#5aa0a0 25%,#2f8fb4 45%,#1e7aa8 100%)" role="img" aria-label="Dolphin leaping from the estuary water"></div>
  <svg class="wave" style="top:360px;height:30px" viewBox="0 0 266 30" preserveAspectRatio="none" aria-hidden="true">
    <path d="M0 0 L266 0 L266 10 C180 0 80 0 0 20 Z" fill="var(--pale)"/>
  </svg>
</section>

<!-- inside: facilities -->
<section class="panel row-bottom col-3 facilities">
  <h2 class="heading">FACILITIES</h2>
  <ul class="bullets">
    <li>EFTPOS</li>
    <li>Swimming Pool</li>
    <li>Undercover BBQ</li>
    <li>Crab Cooker</li>
    <li>Playground</li>
    <li>Laundrette</li>
    <li>TV Room</li>
    <li>Games Room</li>
  </ul>
  <div class="nearby">
    <div><span>2</span>supermarkets within 2 mins</div>
    <div><span>13</span>take-away shops within 7 mins</div>
    <div><span>6</span>Restaurants within 7mins</div>
    <div><span></span>Mandurah CBD 15 mins</div>
  </div>
  <div class="photo" style="top:360px;height:204px;background:linear-gradient(170deg,#7a9a80 0%,#2a8fb0 40%,#1d6f92 70%,#8a8a7a 100%)" role="img" aria-label="Aerial view of the estuary cut, canals and bridge"></div>
  <svg class="wave" style="top:340px;height:40px" viewBox="0 0 266 40" preserveAspectRatio="none" aria-hidden="true">
    <path d="M0 0 L266 0 L266 24 C180 2 80 0 0 22 Z" fill="var(--white)"/>
    <path d="M0 22 C80 0 180 2 266 24" fill="none" stroke="#33b7e6" stroke-width="5"/>
  </svg>
</section>

</body>
</html>
```